Flyer-Design für Beratung, Coaching
Zielgruppe
Beratung, Coaching, Mediation. Meine Zielgruppe sind insbesondere hochgestellte Führungskräfte /Bereichsleiter, Vorstände, Geschäftsführer und Projektleiter.
Aufgabenstellung
Ich habe das neue Logo (quervoran.kollegen), den ersten Flyer, ein neues Bild und den aktuellen Text des Flyers beigefügt. beigefügt. Ich müsste im fertigen Flyer aber den Text editieren können, da ich gelegentlich neue Passagen einfügen möchte. Der Flyer sollte DIN A4 quer im Format sein, damit ich ihn falten kann. Sofern aber jemand eine andere Idee hat, nur zu. Farblich sollte natürlich das neue Logo die Gestaltung des Flyers beeinflussen. Der Flyer soll als eher exklusives Giving verwendet werden; nicht als 'Massenware'. Ich möchte den Flyer als persönliches Profildokument an ausgewählte Personen weitergeben, die mich bereits aus der Mund-zu-Mund Propaganda kennen.

```html
<!DOCTYPE html>
<html lang="de">
<head>
<meta charset="utf-8">
<title>Profilflyer Martin K. Halberg</title>
<link href="https://fonts.googleapis.com/css2?family=Raleway:wght@400;500;700&display=swap" rel="stylesheet">
<style>
  :root{
    --stage:#4a4a4a;
    --teal:#1d6066;
    --gold:#a88227;
    --gold-text:#a47c26;
    --head:#1d5e66;
    --white:#ffffff;
    --photo-dark:#2b2420;
    --photo-mid:#6e5a4a;
  }
  *{margin:0;padding:0;box-sizing:border-box}
  html,body{width:1034px;height:1200px;overflow:hidden;background:var(--stage)}
  body{position:relative;font-family:'Raleway',sans-serif;font-feature-settings:"onum" 1}
  .panel{position:absolute;height:496px;overflow:hidden}
  .panel svg.shapes{position:absolute;inset:0;width:100%;height:100%}
  .shapes polygon{filter:drop-shadow(2px 3px 4px rgba(0,0,0,.35))}

  /* outer sheet */
  .profile{left:167px;top:79px;width:241px;background:var(--white);padding:0 14px 0 29px}
  .contact-panel{left:408px;top:79px;width:219px;background:var(--teal)}
  .cover{left:627px;top:79px;width:240px}

  .brand{display:flex;align-items:center;justify-content:center;gap:5px;margin:72px 0 0 -15px;color:var(--gold-text);font-size:12.5px;font-weight:500}
  .brand-dot{width:6px;height:6px;border-radius:50%;background:var(--gold)}
  h2{font-weight:500;color:var(--head);font-size:10.5px;letter-spacing:-.1px}
  .profile h2{margin-top:12px;margin-bottom:3px}
  .profile h2.first{margin-top:17px}
  .qual p{font-size:6.8px;line-height:8.2px;color:var(--gold-text);margin-bottom:4px}
  .career{font-size:6.8px;line-height:12.4px;color:var(--gold-text)}
  .profile h2.cert{margin-top:3px}
  .badges{display:flex;align-items:center;gap:8px;margin:12px 0 9px}
  .badge-square{width:40px;height:36px;background:#b9b9b9}
  .badge-circle{width:36px;height:36px;border-radius:50%;background:#1e4f9a}
  .badge-circle.light{background:#1d8fd1}
  .awards p{font-size:6.8px;line-height:8px;color:var(--gold-text);margin-bottom:5px}

  .contact{position:absolute;left:13px;top:339px;color:var(--white)}
  .contact h2{color:var(--white);font-size:13px;margin-bottom:10px}
  .contact p{font-size:7px;line-height:12.5px}
  .contact .gap{height:12px}

  .photo{position:absolute;inset:0;background:radial-gradient(ellipse at 55% 45%,var(--photo-mid) 0%,#4a3b31 45%,var(--photo-dark) 100%)}
  .cover-title{position:absolute;right:13px;top:12px;text-align:left;color:var(--white)}
  .cover-title h1{font-weight:400;font-size:18px;line-height:20px}
  .cover-title p{font-size:7.2px;margin-top:1px}
  .claim{position:absolute;right:10px;top:381px;text-align:right;color:var(--white);font-weight:700;font-size:8.3px;line-height:12.4px}

  /* inner sheet */
  .inner-left{left:167px;top:625px;width:219px;background:var(--teal)}
  .services{left:386px;top:625px;width:413px;background:var(--white);padding:24px 20px 0 23px;box-shadow:-4px 0 8px rgba(0,0,0,.35);z-index:2;color:var(--gold-text)}
  .inner-right{left:799px;top:625px;width:68px;background:var(--teal)}
  .services h2{font-size:11px;margin-bottom:7px}
  .services .text{font-size:5.6px;line-height:10px}
  .services .sub{padding-left:10px}
  .services .sub h2{margin-top:8px;margin-bottom:6px}
  .services h2.fields{margin-top:9px;margin-bottom:6px}
  .services .closing{font-weight:700;margin-top:18px}
</style>
</head>
<body>

<!-- outer sheet -->
<section class="panel profile">
  <div class="brand"><span class="brand-dot"></span>quervoran.kollegen</div>
  <h2 class="first">Qualifikation</h2>
  <div class="qual">
    <p>Dipl. Betriebswirt<br>Mainzer Hochschule für<br>Finanzwirtschaft – 4 Jahre</p>
    <p>Bankkaufmann IHK</p>
    <p>Coach (DCB) 2 Jahre<br>gfbo – Gesellschaft für Führungs- und<br>Beratungskompetenz</p>
    <p>General Management Programm<br>Genobund Gruppe, 2 Jahre Spree Management Institut</p>
  </div>
  <h2>Beruflicher Werdegang</h2>
  <p class="career">Nach Berufsausbildung zunächst im (internationalen)<br>Kreditgeschäft tätig. Wechsel zur Rheinauer Bank im Oktober<br>1990 und berufsintegriertes Studium an der Mainzer Hochschule<br>für Finanzwirtschaft. Bis 2002 Direktor Personal.<br>Wechsel 2003 zur Taunus Kapitalbank als Global Head HR. 2009<br>erneuter Wechsel zur Rheinauer Bank als Global Head Personal,<br>Verwaltung und Marketing. Mitglied im Kreditkomittee. Mitte<br>2010 Wechsel zur Hessen Privatbank als Global Head HR &amp;<br>Changemanagement.</p>
  <h2 class="cert">Zertifizierungen &amp; Auszeichnungen</h2>
  <div class="badges">
    <div class="badge-square"></div>
    <div class="badge-circle"></div>
    <div class="badge-circle light"></div>
  </div>
  <div class="awards">
    <p>Preisträger Hessischer Trainingspreis 2004</p>
    <p>Preisträger Hessischer Personalwirtschafts-<br>&nbsp;preis 2007</p>
  </div>
</section>

<section class="panel contact-panel">
  <svg class="shapes" viewBox="0 0 219 496" preserveAspectRatio="none" aria-hidden="true">
    <polygon points="0,0 95,0 171,102 0,231" fill="var(--gold)"/>
    <polygon points="146,444 219,383 219,496 179,496" fill="var(--gold)"/>
  </svg>
  <div class="contact">
    <h2>Kontakt</h2>
    <p>Martin K. Halberg<br>Ahornweg 4<br>61137 Schöneck/Hess</p>
    <div class="gap"></div>
    <p>Phone +49 6101 555218<br>Mobil +49 170 55501843<br>Mail mhalberg@quervoran.kollegen<br>Web www.quervoran.kollegen</p>
  </div>
</section>

<section class="panel cover">
  <div class="photo" role="img" aria-label="Porträtfoto des Beraters mit Brille, Hand am Kinn, warmer dunkler Hintergrund"></div>
  <svg class="shapes" viewBox="0 0 240 496" preserveAspectRatio="none" aria-hidden="true">
    <polygon points="240,304 240,496 108,496 30,417" fill="var(--gold)"/>
  </svg>
  <div class="cover-title">
    <h1>Martin K. Halberg</h1>
    <p>Position Counseling – Coaching</p>
  </div>
  <p class="claim">Um als Top-Führungsperson<br>erfolgreich zu sein, interessieren<br>nicht die Leistungen der<br>Vergangenheit; entscheidend<br>sind die richtige Positionierung,<br>geschicktes strategisches<br>Handeln und die persönliche<br>kollegiale Interaktion.</p>
</section>

<!-- inner sheet -->
<section class="panel inner-left">
  <svg class="shapes" viewBox="0 0 219 496" preserveAspectRatio="none" aria-hidden="true">
    <polygon points="0,0 95,0 171,102 0,232" fill="var(--gold)"/>
    <polygon points="146,443 219,381 219,496 179,496" fill="var(--gold)"/>
  </svg>
</section>

<section class="panel services">
  <h2>Meine Leistungen</h2>
  <p class="text">Ich unterstütze Führungspersonen in Spitzenpositionen bei: Erfolgreicher Bewältigung anspruchsvoller Managementphasen.<br>Übernahme einer neuen Position, herausfordernden strategischen Implementierungen, Turnaroundsituationen. Begleitung in<br>Konflikten im obersten Führungsteam, sensiblen personellen Einzelsituationen auf den Topebenen und bei der Umsetzung<br>personalpolitisch herausfordernder Maßnahmen. Moderation von Konflikten zwischen Eigentümer, Aufsichtsgremium und<br>oberster Führungsebene. Zielgruppen: Top-Führungspersonen, Vorstände und Aufsichtsräte. Tätigkeitsbereiche: Coaching,<br>Executive Advisory, Restrukturierungen und Change Management.</p>
  <div class="sub">
    <h2>Position Counseling</h2>
    <p class="text">Individuelle Einzelberatung, die sich ganz mit der Person und dem Kontext der aktuellen Herausforderungen befasst. 360°<br>Check auf alle vernetzten (Teil-)Aspekte von Managementthemen, Transformations-Prozesse und mikropolitischen<br>Verhältnissen. Trittsicherheit und die Festigung der aktuellen Position stehen hierbei im Mittelpunkt meiner Unterstüt-<br>zungsleistungen.<br>– Umfeldanalyse<br>– Strategieentwicklung<br>– Strategien für Positionsgewinnung,<br>&nbsp;&nbsp;&nbsp;Positionserhalt und -erweiterung<br>– Konfliktbearbeitung</p>
    <h2>Coaching</h2>
    <p class="text">Professionelle Beratung, Begleitung und Unterstützung zur Steigerung und dem Erhalt der Leistungsfähigkeit. Im Coaching<br>unterstütze ich die persönliche und berufliche Weiterentwicklung, die Selbstorganisation und das Selbstverständnis. Der Klient<br>erhält die Möglichkeit, über sich selbst nachzudenken, neue Fähigkeiten zu erlernen und neue Perspektiven einzunehmen.</p>
  </div>
  <h2 class="fields">Erfahrungsfelder</h2>
  <p class="text">&nbsp;- Aufsichtsratsmandate in der Beratungsbranche für interaktive Lernmedien seit 2001 und im betrieblichen<br>&nbsp;&nbsp;&nbsp;Gesundheitsmanagement seit 2012<br>– Sparingspartner und Berater für Vorstand und Aufsichtsrat<br>– Verantwortung für unternehmensweite Restrukturierungen und Personalabbau<br>– Leitung von Kostensenkungs- und Effiziensteigerungsprojekten<br>– Krisenmanagement, Krisenkommunikation<br>– Leitung von mehrjährigen Changemanagementprojekten<br>– Aufbau und Neuausrichtung von Organisationseinheiten<br>– Führung von Einheiten mit über 200 Mitarbeitern</p>
  <p class="text closing">Seit über 20 Jahren in großen Inhouseprojekten und als externer Berater<br>und Coach tätig.</p>
</section>

<section class="panel inner-right">
  <svg class="shapes" viewBox="0 0 68 496" preserveAspectRatio="none" aria-hidden="true">
    <polygon points="0,0 68,0 68,179 0,232" fill="var(--gold)"/>
  </svg>
</section>

</body>
</html>
```